Townhome Multi-Family Property Exterior Sign

Hello. We are looking for a new design for our exterior pylon for for a multi-family housing property in Texas. The design will need to go on a new sign panel to replace the existing (see photo of existing). We are looking to see both modern and contemporary designs. Included the sign should be the name, Loma Brisa Townhomes and the web address www.lomabrisatownhomes.example.

Attached here is a PDF file of the proposed new sign shape. We are open to other shape ideas as well if your design would better suit a more rectangular shape.

Industry/Entity Type

Property

Font styles to use
Serif
Sans Serif

Colors
9bcb3c

Requirements
Must have
• Name of building: Loma Brisa Townhomes
• Website: www.lomabrisatownhomes.example
Nice to have
• Address: 420-530 Halvorsen Lane (only if it fits nicely)

```html
<!DOCTYPE html>
<html lang="en">
<head>
<meta charset="utf-8">
<title>Loma Brisa Townhomes – Exterior Sign Panel</title>
<link rel="stylesheet" href="https://fonts.googleapis.com/css2?family=Tinos:wght@700&display=swap">
<style>
  :root {
    --backdrop: #e4e4e4;
    --panel-charcoal: #333333;
    --sign-green: #22744a;
    --sign-green-edge: #1e6a41;
    --sign-white: #ffffff;
    --ink-dark: #262626;
  }
  html, body {
    margin: 0;
    padding: 0;
    width: 1200px;
    height: 729px;
    overflow: hidden;
    background: var(--backdrop);
  }
  .sign {
    display: block;
    width: 1200px;
    height: 729px;
  }
  .sign-text {
    font-family: "Tinos", "Times New Roman", serif;
    font-weight: 700;
  }
  .property-name { fill: var(--sign-white); font-size: 116px; }
  .property-type { fill: var(--sign-white); font-size: 56px; }
  .property-web  { fill: var(--ink-dark); font-size: 44px; }
  .panel-back   { fill: var(--panel-charcoal); }
  .face-edge    { fill: var(--sign-green-edge); }
  .face         { fill: var(--sign-green); }
  .web-band     { fill: var(--sign-white); }
</style>
</head>
<body>
<svg class="sign" viewBox="0 0 1200 729" xmlns="http://www.w3.org/2000/svg">
  <defs>
    <filter id="panel-shadow" x="-10%" y="-10%" width="120%" height="125%">
      <feDropShadow dx="4" dy="6" stdDeviation="5" flood-color="#000" flood-opacity="0.35"/>
    </filter>
    <filter id="letter-shadow" x="-5%" y="-10%" width="110%" height="130%">
      <feDropShadow dx="2" dy="3" stdDeviation="1.5" flood-color="#000" flood-opacity="0.45"/>
    </filter>
  </defs>

  <!-- back panel -->
  <rect class="panel-back" x="219" y="105" width="908" height="516" filter="url(#panel-shadow)"/>

  <!-- green sign face with edge layer -->
  <rect class="face-edge" x="80" y="190" width="970" height="367"/>
  <rect class="face" x="70" y="180" width="970" height="369" filter="url(#panel-shadow)"/>

  <!-- web address band -->
  <rect class="web-band" x="70" y="441" width="970" height="73"/>

  <g class="sign-text" filter="url(#letter-shadow)">
    <text class="property-name" x="943" y="328" text-anchor="end" textLength="790" lengthAdjust="spacingAndGlyphs">LOMA BRISA</text>
    <text class="property-type" x="943" y="401" text-anchor="end" textLength="420" lengthAdjust="spacingAndGlyphs">TOWNHOMES</text>
  </g>
  <text class="sign-text property-web" x="157" y="492" textLength="786" lengthAdjust="spacingAndGlyphs">www.LomaBrisaTownHomes.example</text>
</svg>
</body>
</html>
```